Amber Ridge Partners Business Card

A business card design to accompany the logo design you completed on Pixel Forum. We are open to your proposals. I did add one idea below that might work, but we aren't married to the idea. The company is a real estate services company. Clientele are typically high net worth individuals, executive level employment or owners of their own company, 30-60 years old.

Our 1 (bad?) idea: double sided card; One side landscape with logo and word mark. Other side Portrait with the logo only (oversize watermark maybe?). Somewhere add text of Name (Marcus Tellingham), Title (Principal), phone # (555-214-7736) and email address (marcus@amberridgeco.example). There would be a second design with my wife's name, number and email in place of mine.

Again totally open to ideas here.

Industry/Entity Type

Real Estate

```html
<!DOCTYPE html>
<html lang="en">
<head>
<meta charset="utf-8">
<title>Amber Ridge Partners — Business Card</title>
<link rel="stylesheet" href="https://fonts.googleapis.com/css2?family=Arimo:wght@400&family=Cinzel:wght@400&display=swap">
<style>
  :root {
    --backdrop: #ececec;
    --card: #ffffff;
    --sage: #7f9f70;
    --sage-light: #a9bf9c;
    --stone: #9a9a9a;
    --stone-dark: #8a8a8a;
    --text-soft: #a3a3a3;
  }
  * { margin: 0; padding: 0; box-sizing: border-box; }
  html, body {
    width: 1200px;
    height: 720px;
    overflow: hidden;
    background: var(--backdrop);
  }
  .canvas {
    position: relative;
    width: 1200px;
    height: 720px;
  }
  .card {
    position: absolute;
    top: 210px;
    width: 525px;
    height: 300px;
    background: var(--card);
    overflow: hidden;
    box-shadow: 0 2px 10px rgba(0, 0, 0, 0.08);
  }
  .card--contact { left: 50px; }
  .card--brand { left: 625px; }

  /* Contact side */
  .contact {
    position: absolute;
    left: 40px;
    bottom: 52px;
    font-family: "Arimo", Helvetica, Arial, sans-serif;
  }
  .contact__name {
    font-size: 25px;
    color: var(--sage-light);
    line-height: 1;
  }
  .contact__title {
    font-size: 17px;
    color: var(--text-soft);
    margin-top: 4px;
  }
  .contact__detail {
    font-size: 17px;
    color: var(--text-soft);
    margin-top: 22px;
  }
  .contact__detail + .contact__detail { margin-top: 14px; }

  /* Brand side */
  .band {
    position: absolute;
    left: 0;
    width: 100%;
    height: 34px;
    background: var(--sage);
  }
  .band--top { top: 0; }
  .band--bottom { bottom: 0; }
  .rule {
    position: absolute;
    left: 0;
    width: 100%;
    height: 3px;
    background: var(--stone);
  }
  .rule--top-a { top: 44px; }
  .rule--top-b { top: 52px; }
  .rule--bottom-a { bottom: 52px; }
  .rule--bottom-b { bottom: 44px; }

  .wordmark {
    position: absolute;
    top: 50%;
    left: 50%;
    transform: translate(-50%, -50%);
    display: flex;
    align-items: center;
    gap: 18px;
    white-space: nowrap;
  }
  .wordmark__dot {
    width: 34px;
    height: 34px;
    border-radius: 50%;
    background: var(--sage);
    flex: none;
  }
  .wordmark__name {
    font-family: "Cinzel", "Trajan Pro", Georgia, serif;
    font-size: 30px;
    letter-spacing: 1px;
    color: var(--sage);
  }
</style>
</head>
<body>
  <main class="canvas">
    <section class="card card--contact" aria-label="Card back with contact details">
      <div class="contact">
        <p class="contact__name">Marcus Tellingham</p>
        <p class="contact__title">Principal</p>
        <p class="contact__detail">marcus@amberridgeco.example</p>
        <p class="contact__detail">555-214-7736</p>
      </div>
    </section>

    <section class="card card--brand" aria-label="Card front with company name">
      <div class="band band--top"></div>
      <div class="rule rule--top-a"></div>
      <div class="rule rule--top-b"></div>

      <div class="wordmark">
        <span class="wordmark__dot"></span>
        <span class="wordmark__name">Amber Ridge Partners</span>
      </div>

      <div class="rule rule--bottom-a"></div>
      <div class="rule rule--bottom-b"></div>
      <div class="band band--bottom"></div>
    </section>
  </main>
</body>
</html>
```